Business Card for Amber Heron Advisors

Business card design for Amber Heron Advisors, a new consulting and financial advisory firm. I would like the designs to integrate the logo attached (at least on 1 side).

Target Market(s)

individual and institutional clients

Contact Information for Business Card

Dominic L. Hartwell, CFA
Managing Director
amberheronadvisors.examplep
hartwell@amberheronadvisors.example
(555) 218-4903

```html
<!DOCTYPE html>
<html lang="en">
<head>
<meta charset="utf-8">
<title>Amber Heron Advisors — Business Card</title>
<link rel="stylesheet" href="https://fonts.googleapis.com/css2?family=Josefin+Sans:wght@400;600&family=League+Spartan:wght@700&display=swap">
<style>
  :root {
    --backdrop: #202020;
    --card: #121212;
    --card-edge: #1a1a1a;
    --amber: #e5891f;
    --ink-light: #f1f1f1;
  }
  * { box-sizing: border-box; margin: 0; padding: 0; }
  html, body {
    width: 1189px;
    height: 1200px;
    overflow: hidden;
    background: var(--backdrop);
  }
  .canvas {
    position: relative;
    width: 1189px;
    height: 1200px;
  }
  .card {
    position: absolute;
    left: 173px;
    width: 854px;
    height: 486px;
    border-radius: 37px;
    background: radial-gradient(ellipse at 50% 20%, var(--card-edge), var(--card) 70%);
    color: var(--ink-light);
    text-align: center;
  }
  .card--front { top: 69px; }
  .card--back { top: 627px; }

  .brand-name {
    position: absolute;
    left: 0;
    right: 0;
    top: 214px;
    font-family: "Josefin Sans", sans-serif;
    font-weight: 600;
    font-size: 50px;
    letter-spacing: 1px;
    text-transform: uppercase;
    color: var(--amber);
  }

  .holder-name {
    position: absolute;
    left: 0;
    right: 0;
    top: 144px;
    font-family: "League Spartan", sans-serif;
    font-weight: 700;
    font-size: 30px;
    letter-spacing: 0.5px;
    color: var(--amber);
  }
  .holder-title {
    position: absolute;
    left: 0;
    right: 0;
    top: 180px;
    font-family: "Josefin Sans", sans-serif;
    font-size: 20px;
    letter-spacing: 0.6px;
  }
  .contact {
    position: absolute;
    left: 0;
    right: 0;
    top: 280px;
    font-family: "Josefin Sans", sans-serif;
    font-size: 21px;
    letter-spacing: 0.5px;
    line-height: 29px;
    list-style: none;
  }
  .contact__web { margin-top: 8px; }
  .contact__domain { color: var(--amber); }
</style>
</head>
<body>
<main class="canvas">
  <section class="card card--front" aria-label="Card front">
    <h1 class="brand-name">Amber Heron Advisors</h1>
  </section>

  <section class="card card--back" aria-label="Card back">
    <h2 class="holder-name">DOMINIC L. HARTWELL, CFA</h2>
    <p class="holder-title">Managing Director</p>
    <ul class="contact">
      <li class="contact__phone">(555) 218-4903</li>
      <li class="contact__email">hartwell@amberheronadvisors.example</li>
      <li class="contact__web"><span class="contact__domain">amberheronadvisors</span>.example</li>
    </ul>
  </section>
</main>
</body>
</html>
```